Across Amber Fields Oz Tour Flyer

I need a dynamic flyer for a concert tour.
I have uploaded the file. Please use these ingredients for the design.
The font for the title is Jellyka Jellyfish lower case from www.glyphbarn-example.net
We are getting close!! We just need bright colours, the headings to STAND OUT and Byron Bay has to be moved to under NSW Bellingen.
Thanks for all your hard work!
We are targeting a wide range of customers from old age to children and families
Tour

```html
<!DOCTYPE html>
<html lang="en">
<head>
<meta charset="utf-8">
<title>Across Amber Fields – Tour Flyer</title>
<link rel="stylesheet" href="https://fonts.googleapis.com/css2?family=Sacramento&family=Bebas+Neue&family=Lato:wght@700&family=Roboto+Condensed:wght@700&display=swap">
<style>
  :root {
    --gold: #d9cb4a;
    --gold-deep: #c4b43a;
    --red: #c4000b;
    --ink: #1c1c1a;
    --panel: #2e2d2a;
    --panel-deep: #1f1e1c;
    --yellow-text: #f5e100;
    --white: #ffffff;
    --frame: #e9df8c;
  }
  * { margin: 0; padding: 0; box-sizing: border-box; }
  html, body { width: 900px; height: 1200px; overflow: hidden; background: #ffffff; }
  .flyer {
    position: relative; width: 900px; height: 1200px; overflow: hidden;
    background: radial-gradient(ellipse at 50% 40%, var(--gold) 0%, var(--gold-deep) 100%);
  }
  .band { position: absolute; left: 0; width: 100%; }
  .band--title { top: 47px; height: 153px; background: linear-gradient(180deg, var(--red) 0%, #b0000a 100%); }
  .band--venues { top: 425px; height: 449px; background: radial-gradient(ellipse at 70% 50%, var(--panel) 0%, var(--panel-deep) 100%); }
  .band--contact { top: 874px; height: 198px; background: linear-gradient(180deg, var(--red) 0%, #b3000a 100%); }

  .tour-title {
    position: absolute; top: 47px; left: 0; width: 100%; height: 153px;
    display: flex; align-items: center; justify-content: center;
    font-family: "Sacramento", cursive; font-weight: 400; font-size: 96px; line-height: 1;
    white-space: nowrap; color: var(--white);
  }
  .choir-name {
    position: absolute; top: 228px; left: 0; width: 100%; text-align: center;
    font-family: "Bebas Neue", "Arial Narrow", sans-serif; font-weight: 400; font-size: 70px; line-height: 1;
    color: var(--ink); letter-spacing: 0.5px;
  }
  .tour-label {
    position: absolute; top: 298px; left: 0; width: 100%; text-align: center;
    font-family: "Lato", Arial, sans-serif; font-weight: 700; font-size: 38px; color: var(--red);
  }

  .photo-frame {
    position: absolute; left: 49px; top: 373px; width: 437px; height: 798px;
    background: var(--frame); padding: 11px;
    box-shadow: 0 0 14px rgba(0,0,0,0.45);
  }
  .photo {
    width: 100%; height: 100%;
    background: linear-gradient(160deg, #7a4a1c 0%, #b0641c 30%, #e08a1a 55%, #a0301a 78%, #2a1a12 100%);
  }

  .venues { font-family: "Roboto Condensed", "Arial Narrow", sans-serif; font-weight: 700; }
  .region { position: absolute; color: var(--white); font-size: 17.5px; line-height: 24px; }
  .region h3 { color: var(--yellow-text); font-size: 23px; line-height: 26px; font-weight: 700; margin-bottom: 3px; }
  .region ul { list-style: none; }
  .region--vic { left: 535px; top: 462px; }
  .region--act { left: 535px; top: 633px; }
  .region--nsw { left: 748px; top: 462px; }
  .region--qld-a { left: 535px; top: 786px; }
  .region--qld-b { left: 748px; top: 786px; }

  .qld-ribbon {
    position: absolute; left: 600px; top: 734px; width: 260px; height: 34px;
    background: linear-gradient(90deg, rgba(196,0,11,0) 0%, var(--red) 22%, var(--red) 78%, rgba(196,0,11,0) 100%);
    color: var(--yellow-text); text-align: center;
    font-family: "Roboto Condensed", "Arial Narrow", sans-serif; font-weight: 700; font-size: 22px; line-height: 34px;
  }

  .contact { position: absolute; left: 535px; top: 898px; font-family: "Roboto Condensed", "Arial Narrow", sans-serif; font-weight: 700; }
  .contact__label { color: var(--yellow-text); font-size: 29px; line-height: 34px; }
  .contact__value { color: var(--white); font-size: 38px; line-height: 46px; margin-bottom: 2px; white-space: nowrap; }

  .partner {
    position: absolute; top: 1098px; height: 78px;
    display: flex; align-items: center; justify-content: center; gap: 6px;
    font-family: "Roboto Condensed", "Arial Narrow", sans-serif; font-weight: 700; font-size: 17px;
  }
  .partner--harmonia { left: 602px; width: 94px; background: #000; color: var(--white); }
  .partner--savanna { left: 723px; width: 149px; background: var(--white); color: var(--ink); }
  .partner__dot { width: 10px; height: 10px; border-radius: 50%; background: var(--red); }
</style>
</head>
<body>
<main class="flyer">
  <div class="band band--title"></div>
  <div class="band band--venues"></div>
  <div class="band band--contact"></div>

  <h1 class="tour-title">Across Amber Fields</h1>
  <h2 class="choir-name">THE SAVANNA YOUTH SINGERS</h2>
  <p class="tour-label">Australia Tour</p>

  <div class="photo-frame">
    <div class="photo" role="img" aria-label="Photo of a young singer dancing on stage in a yellow dress and straw skirt, with other performers behind"></div>
  </div>

  <section class="venues">
    <div class="region region--vic"><h3>VICTORIA</h3><ul><li>Geelong</li><li>Sunbury</li><li>Melbourne</li><li>Bendigo</li><li>Albury</li></ul></div>
    <div class="region region--act"><h3>A.C.T.</h3><ul><li>Canberra</li></ul></div>
    <div class="region region--nsw"><h3>N.S.W.</h3><ul><li>Nowra</li><li>Sydney</li><li>Wollongong</li><li>Blue Mountains</li><li>Port Macquarie</li><li>Laurieton</li><li>Taree</li><li>Bellingen</li><li>Byron Bay</li></ul></div>
    <div class="qld-ribbon">QLD</div>
    <div class="region region--qld-a"><ul><li>Gold Coast</li><li>Sunshine Coast</li></ul></div>
    <div class="region region--qld-b"><ul><li>Brisbane</li><li>VICTORIA</li></ul></div>
  </section>

  <section class="contact">
    <p class="contact__label">DANA KELLERBY</p>
    <p class="contact__value">0491 570 156</p>
    <p class="contact__label">TICKETS &amp; INFO</p>
    <p class="contact__value">www.amberfields.org</p>
  </section>

  <div class="partner partner--harmonia">Harmonia</div>
  <div class="partner partner--savanna"><span class="partner__dot"></span>Savanna Youth</div>
</main>
</body>
</html>
```